Welding Fabrication and Inspection Business Card Design

Welding Fabrication and Inspection Services,

Business

Industrial Machinery ServicesMohammed Rahim30 Ballarat Street, Mount Gravatt East.4122.QLD

```html
<!DOCTYPE html>
<html lang="en">
<head>
<meta charset="utf-8">
<title>Tarnwell Forge Services – Business Card</title>
<link href="https://fonts.googleapis.com/css2?family=Ubuntu:wght@400;700&display=swap" rel="stylesheet">
<style>
  :root {
    --stage: #e9e6e1;
    --ink: #0b0b0b;
    --paper: #ffffff;
    --card-shadow: rgba(0, 0, 0, 0.18);
  }
  html, body {
    margin: 0;
    padding: 0;
    width: 1200px;
    height: 900px;
    overflow: hidden;
    background: var(--stage);
    font-family: "Ubuntu", sans-serif;
  }
  .stage {
    position: relative;
    width: 1200px;
    height: 900px;
  }
  .card {
    position: absolute;
    left: 280px;
    width: 640px;
    height: 366px;
    overflow: hidden;
    box-shadow: 0 6px 18px var(--card-shadow);
  }
  .card--back {
    top: 64px;
    background: var(--ink);
  }
  .card--front {
    top: 470px;
    background: var(--paper);
    color: var(--ink);
  }
  .wordmark {
    position: absolute;
    display: flex;
    align-items: center;
    gap: 12px;
    font-weight: 700;
    font-size: 23px;
    letter-spacing: 0.2px;
    white-space: nowrap;
  }
  .wordmark__square {
    width: 18px;
    height: 18px;
  }
  .card--back .wordmark {
    left: 50%;
    top: 50%;
    transform: translate(-50%, -50%);
    color: var(--paper);
  }
  .card--back .wordmark__square { background: var(--paper); }
  .card--front .wordmark {
    right: 46px;
    top: 180px;
    color: var(--ink);
  }
  .card--front .wordmark__square { background: var(--ink); }
  .corner-mark {
    position: absolute;
    left: 0;
    top: 18px;
  }
  .holder-name {
    position: absolute;
    left: 80px;
    top: 28px;
    margin: 0;
    font-size: 20px;
    font-weight: 700;
  }
  .address {
    position: absolute;
    left: 44px;
    top: 226px;
    margin: 0;
    font-style: normal;
    font-size: 17px;
    line-height: 1.3;
  }
  .bottom-band {
    position: absolute;
    left: 0;
    bottom: 18px;
  }
</style>
</head>
<body>
  <main class="stage">
    <section class="card card--back" aria-label="Card back">
      <div class="wordmark">
        <span class="wordmark__square"></span>
        <span class="wordmark__name">Tarnwell Forge Services</span>
      </div>
    </section>

    <section class="card card--front" aria-label="Card front">
      <svg class="corner-mark" width="58" height="40" viewBox="0 0 58 40" aria-hidden="true">
        <rect width="58" height="40" fill="var(--ink)"/>
        <polygon points="40,3 45,3 20,37 15,37" fill="var(--paper)"/>
      </svg>
      <h1 class="holder-name">Khalid Nasser</h1>

      <div class="wordmark">
        <span class="wordmark__square"></span>
        <span class="wordmark__name">Tarnwell Forge Services</span>
      </div>

      <address class="address">17 Corrowen Street, Mount<br>Corrin East. 4187.QLD</address>

      <svg class="bottom-band" width="640" height="30" viewBox="0 0 640 30" aria-hidden="true">
        <polygon points="0,0 222,0 208,30 0,30" fill="var(--ink)"/>
        <polygon points="232,0 640,0 640,30 218,30" fill="var(--ink)"/>
      </svg>
    </section>
  </main>
</body>
</html>
```